Companybrochure for Consulting & Financing Firm

I need to have a Company Brochure asap for our company. We have a website that describes what we do, but we need also a brochure, that can be sent by PDF of eventually be printed as well.

The brochure should be short but nice and appealing to the customers.

We provide professional management consulting and help our customers to get finance for very diferent projects. Our business has a lot to do with personal relations, but also we are very professional in the way we work and how develop the solutions for our clients. Our clients are mainly government-owned firm, but also private trading companies and wealthy private investors.

Our customers are mainly in Latin America, but the company is headquater is in Switzerland. We are opening offices in Panama and Caracas, this should be easaly be adabtable later.

Please have a look at our website www.brevalto.ch. In the brochure, we would segment our services in 1.) Project Developments 2.) Management Conulting 3.) Investment Management and 4.) Finance Solutions.

Also do have a look at www.brevalto.ch
(Click E for the English version)

I managed to put the Mock-Up to the Website.
It is actually not really a mock-up, it is a version I have designed myself.
Well as I am not a designer, I hope you can make it much better.
The content however is what I would put in any other design as well.

Target Market(s)

Top Management, Investors, Entrepreneurs, Government Officials

Industry/Entity Type

Management Consulting

Requirements
Must have
• Design should reflect this image elements:

We are entrepreneurs.
We are comitted to get things done.
We work closely with the client side by side.
We are a professional partner.
We are not afraid of delivering unconventional solutions.
We look at the problem from various angles.
We analyse, develop solutions and implent results.
Should not have
• Typical US-American style elements. We do not want to give the impression of being a US company.

We do not want to appear to be neo-liberal. We are a politically neutral professional consulting firm.

```html
<!DOCTYPE html>
<html lang="en">
<head>
<meta charset="utf-8">
<title>Brevalto AG – Company Brochure</title>
<link href="https://fonts.googleapis.com/css2?family=Arimo:wght@400;700&display=swap" rel="stylesheet">
<style>
  :root {
    --ink: #1d1d1f;
    --sky-blue: #2b9bd6;
    --navy: #0c2f6b;
    --royal: #1460ad;
    --stripe: #bcd9f0;
    --bar-grey: #c9cacc;
    --white: #ffffff;
    --paper: #ffffff;
  }
  * { box-sizing: border-box; margin: 0; padding: 0; }
  html, body { width: 896px; height: 1200px; overflow: hidden; background: var(--paper); }
  body { font-family: "Arimo", Arial, sans-serif; color: var(--ink); }
  .brochure { position: relative; width: 896px; height: 1200px; overflow: hidden; background: var(--paper); }
  .backdrop { position: absolute; inset: 0; }
  .contact-bar {
    position: absolute; top: 0; right: 0; width: 440px; height: 36px;
    background: var(--bar-grey); border-bottom-left-radius: 4px;
    display: flex; align-items: center; justify-content: flex-end; gap: 8px;
    padding-right: 28px; font-size: 17px; color: #333;
  }
  .contact-bar svg { width: 18px; height: 14px; }
  .brand { position: absolute; left: 42px; top: 44px; font-size: 36px; font-weight: 400; color: var(--ink); letter-spacing: -0.5px; }
  .headline {
    position: absolute; left: 42px; top: 128px; width: 720px;
    font-size: 32px; line-height: 40px; font-weight: 400; color: var(--sky-blue);
  }
  .hero-photo { position: absolute; left: 58px; top: 268px; }
  .content { position: absolute; left: 42px; top: 700px; width: 812px; color: var(--white); }
  .company-name { font-size: 36px; font-weight: 400; margin-bottom: 16px; }
  .intro { font-size: 19.5px; line-height: 30px; margin-bottom: 22px; }
  .fields-lead { font-size: 19.5px; margin-bottom: 12px; }
  .fields { list-style: none; display: grid; grid-template-columns: 311px 1fr; row-gap: 8px; font-size: 19.5px; }
  .fields li::before { content: "• "; }
  .note-box {
    position: absolute; left: 42px; top: 1022px; width: 826px; height: 124px;
    background: var(--white); display: flex; align-items: center; justify-content: center;
    padding: 0 28px; text-align: center; font-size: 19px; line-height: 28px; color: var(--sky-blue);
  }
</style>
</head>
<body>
<main class="brochure">
  <svg class="backdrop" width="896" height="1200" viewBox="0 0 896 1200">
    <defs>
      <linearGradient id="panelBlue" x1="0" y1="0" x2="0.4" y2="1">
        <stop offset="0" stop-color="#1a6fbc"/>
        <stop offset="0.45" stop-color="#123f86"/>
        <stop offset="1" stop-color="#0a2a62"/>
      </linearGradient>
    </defs>
    <polygon points="420,300 896,238 896,252 420,316" fill="var(--stripe)" opacity="0.6"/>
    <polygon points="420,322 896,262 896,282 420,344" fill="#7fb6e2" opacity="0.7"/>
    <polygon points="0,350 896,286 896,1200 0,1200" fill="url(#panelBlue)"/>
  </svg>

  <div class="contact-bar">
    <svg viewBox="0 0 18 14" aria-hidden="true"><rect x="0.5" y="0.5" width="17" height="13" rx="1.5" fill="#555"/><path d="M1 1.5 L9 8 L17 1.5" stroke="#ddd" stroke-width="1.4" fill="none"/></svg>
    <span>info@brevalto.com</span>
  </div>

  <div class="brand">Brevalto</div>
  <h1 class="headline">Complete Solutions for Consulting,&nbsp;&nbsp;Financing and Investment Company.</h1>

  <svg class="hero-photo" width="700" height="460" viewBox="0 0 700 460" role="img" aria-label="Photo: businessman holding an umbrella standing in water, surrounded by question marks">
    <defs>
      <linearGradient id="photoTone" x1="0" y1="0" x2="0" y2="1">
        <stop offset="0" stop-color="#ffffff"/>
        <stop offset="0.5" stop-color="#e9ecef"/>
        <stop offset="0.75" stop-color="#b9c0c7"/>
        <stop offset="1" stop-color="#dfe3e6"/>
      </linearGradient>
    </defs>
    <ellipse cx="350" cy="230" rx="340" ry="222" fill="url(#photoTone)" stroke="var(--white)" stroke-width="10"/>
  </svg>

  <section class="content">
    <h2 class="company-name">Brevalto AG</h2>
    <p class="intro">Welcome to Brevalto AG. Our company is a Swiss stock corporation and was established in 1995. As a consulting, financing and investment company, we are primarily committed to companies and projects in Switzerland and Latin America.</p>
    <p class="fields-lead">Brevalto AG operates in the following fields:</p>
    <ul class="fields">
      <li>Project development</li>
      <li>Management Consulting</li>
      <li>Investment finance</li>
      <li>Private equity</li>
    </ul>
  </section>

  <div class="note-box">Lorem ipsum dolor sit amet, consectetuer adipiscing elit, sed diam nonummy nibh euismod tincid unt ut laoreet dolore magna aliquam erat volutpat. Ut wisi enim ad minim veniam.</div>
</main>
</body>
</html>
```